transparent 3D concussion booklet

I need a cutting edge 3 dimensional, layered booklet/brochure that is a layered brain from the outside in as you turn the page you strip off a layer of the brain and go deeper into it. the brain should be in colour and there needs to be room for text on each transparent page to speak on the part of the brain we are focusing on. on the last page the contact information and logo. Below are the sections of the brain needed for each page.

cover page
Intro
pg 1 vision
pg2 vestibular
pg3 somatosensory
pg4 hormone
pg5 physiological
pg6 psychological
pg 7 contact information/logo

Target Market(s)

general population that has fallen, whiplash, sports, hit their head.

Industry/Entity Type

Medical

Font styles to use
Serif

Colors
0255a3
3377b5
85acd3
cedeed
0792cd
33a6d7
85cae6
cadf82
acd136

Requirements
Must have
• the pages requested, be 3D transparent with layers, each page must have space to write text. printable on a mass scale, cutting edge, clean, easy to manipulate. clear graphics, bound like a booklet. professional material not cartoon. different parts of the brain need to be different colours. main clinic collars are blues and greens.
Nice to have
• innovation this is for educational material for general population, doctors, lawyers. has to be used as a learning and educational tool. rectangle in shape.
Should not have
• not larger than half a letter sized piece of paper.

```html
<!DOCTYPE html>
<html lang="en">
<head>
<meta charset="utf-8">
<title>Human Brain Anatomy – Booklet Pages</title>
<link href="https://fonts.googleapis.com/css2?family=Montserrat:wght@300;800&family=Merriweather:wght@300;400&display=swap" rel="stylesheet">
<style>
  :root{
    --backdrop:#e2e2e2;
    --paper:#ffffff;
    --fold:#e4e4e4;
    --ink:#1e1e1e;
    --ink-soft:#6a6a6a;
    --brand-green:#7fa323;
    --brand-lime:#acd136;
    --navy-blue:#0255a3;
    --clinic-blue:#0792cd;
    --sky-blue:#33a6d7;
    --pale-blue:#85cae6;
    --brain-orange:#f0782a;
    --brain-red:#e2364a;
    --brain-grey:#c7bfb4;
  }
  *{box-sizing:border-box;margin:0;padding:0}
  html,body{width:1200px;height:1200px;overflow:hidden}
  body{background:var(--backdrop);font-family:"Merriweather",serif;color:var(--ink);position:relative}

  .page{position:absolute;background:var(--paper);box-shadow:0 2px 6px rgba(0,0,0,.18);overflow:hidden}
  .cover,.back-cover{left:42px;width:264px;height:347px}
  .cover{top:31px;z-index:3}
  .back-cover{top:407px;z-index:3;background:linear-gradient(135deg,#f2f2f2 0%,var(--paper) 45%)}

  .spread{position:absolute;width:424px;height:280px;overflow:hidden;
    background:linear-gradient(to right,var(--paper) 0%,#f4f4f4 44%,#e9e9e9 50%,#f4f4f4 56%,var(--paper) 100%);
    box-shadow:0 2px 6px rgba(0,0,0,.18)}
  .spread::after{content:"";position:absolute;left:212px;top:0;width:1px;height:100%;background:var(--fold)}
  .spread.col-left{left:238px}
  .spread.col-right{left:676px}
  .spread.row-1{top:270px}
  .spread.row-2{top:558px}
  .spread.row-3{top:848px}

  /* cover */
  .cover-title{position:absolute;left:16px;top:22px;font-family:"Montserrat",sans-serif;line-height:1}
  .cover-title .kicker{display:block;font-weight:300;font-size:16px;letter-spacing:.3px}
  .cover-title .main{display:block;font-weight:800;font-size:27px;margin-top:2px}
  .cover-rule{position:absolute;left:16px;top:66px;width:250px;height:5px;background:var(--ink)}
  .cover-author{position:absolute;left:16px;top:77px;font-family:"Merriweather",serif;font-weight:300;font-size:9px;color:var(--ink-soft)}
  .cover-art{position:absolute;left:0;bottom:0;width:264px;height:254px;
    background:radial-gradient(ellipse 48% 40% at 55% 38%,var(--brain-red) 0%,var(--brain-orange) 40%,var(--clinic-blue) 75%,transparent 100%),
               radial-gradient(ellipse 65% 70% at 55% 60%,var(--sky-blue) 0%,var(--navy-blue) 70%,var(--paper) 100%)}

  .brand{font-family:"Montserrat",sans-serif;font-weight:800;color:var(--brand-green);display:flex;align-items:center;gap:4px;line-height:1}
  .brand .dot{display:inline-block;border-radius:50%;background:var(--brand-lime)}
  .brand-tag{display:block;font-family:"Merriweather",serif;font-size:3px;color:var(--ink-soft);letter-spacing:.2px;margin-top:3px}
  .cover-brand{position:absolute;right:16px;top:30px;text-align:right}
  .cover-brand .brand{font-size:11px}
  .cover-brand .dot{width:8px;height:8px}

  /* back cover */
  .back-footer{position:absolute;left:34px;top:258px}
  .back-footer .brand{font-size:10px}
  .back-footer .dot{width:7px;height:7px}
  .contact{margin-top:10px;font-size:3.6px;line-height:1.4;color:var(--ink)}
  .contact-lines{list-style:none;margin-top:5px}
  .contact-lines li{display:flex;align-items:center;gap:3px}
  .contact-lines .bullet{width:2.5px;height:2.5px;background:var(--navy-blue);border-radius:50%}

  /* inner pages */
  .section-title{position:absolute;font-family:"Merriweather",serif;font-weight:300;color:var(--ink-soft);line-height:1}
  .section-title.large{font-size:7px}
  .section-title.small{font-size:4.4px}
  .section-body{position:absolute;font-size:3px;line-height:1.5;color:var(--ink-soft)}
  .section-body p+p{margin-top:4px}

  .head-art{position:absolute;left:256px;top:58px;width:110px;height:136px;border-radius:46% 50% 28% 40% / 44% 48% 36% 36%}
  .head-art.layer-vestibular{background:radial-gradient(circle at 58% 30%,var(--brain-orange) 0 9%,var(--sky-blue) 22%,var(--clinic-blue) 45%,var(--navy-blue) 85%)}
  .head-art.layer-hormone{background:radial-gradient(ellipse 24% 18% at 66% 40%,var(--brain-orange) 0 70%,transparent 100%),radial-gradient(circle at 55% 35%,var(--sky-blue),var(--clinic-blue) 45%,var(--navy-blue) 85%)}
  .head-art.layer-somatosensory{background:radial-gradient(ellipse 22% 16% at 68% 42%,var(--brain-orange) 0 70%,transparent 100%),radial-gradient(circle at 55% 35%,var(--sky-blue),var(--clinic-blue) 45%,var(--navy-blue) 85%)}
  .head-art.layer-physiological{background:radial-gradient(ellipse 44% 30% at 58% 26%,var(--brain-grey) 0 60%,transparent 100%),radial-gradient(circle at 55% 35%,var(--sky-blue),var(--clinic-blue) 45%,var(--navy-blue) 85%)}
  .head-art.layer-psychological{background:radial-gradient(ellipse 44% 30% at 58% 28%,var(--brain-red) 0 40%,var(--brain-orange) 65%,transparent 100%),radial-gradient(circle at 55% 35%,var(--sky-blue),var(--clinic-blue) 45%,var(--navy-blue) 85%)}
</style>
</head>
<body>

<!-- Front cover -->
<section class="page cover">
  <h1 class="cover-title"><span class="kicker">HUMAN BRAIN</span><span class="main">ANATOMY</span></h1>
  <div class="cover-brand">
    <div class="brand"><span class="dot"></span>Neurova</div>
    <span class="brand-tag">brain and spine care</span>
  </div>
  <div class="cover-rule"></div>
  <p class="cover-author">Dr. Alex Morgan</p>
  <div class="cover-art" role="img" aria-label="Translucent 3D illustration of a head in profile with the brain glowing red and orange inside"></div>
</section>

<!-- Back cover -->
<section class="page back-cover">
  <div class="back-footer">
    <div class="brand"><span class="dot"></span>Neurova</div>
    <span class="brand-tag">brain and spine care</span>
    <div class="contact">
      <p>Elm Row,<br>Westbrook,<br>CT 06000</p>
      <ul class="contact-lines">
        <li><span class="bullet"></span>555 0142</li>
        <li><span class="bullet"></span>hello@neurova.example</li>
        <li><span class="bullet"></span>neurova.example</li>
      </ul>
    </div>
  </div>
</section>

<!-- Introduction / Vision -->
<section class="spread col-left row-1">
  <h2 class="section-title large" style="left:78px;top:114px">Introduction</h2>
  <div class="section-body" style="left:78px;top:127px;width:70px">
    <p>A concussion changes how the brain works for a while. This booklet walks through each layer, from the surface to the deep core, and shows which systems may be affected after a fall, a sports hit or whiplash.</p>
    <p>Turn each page to lift one layer away. Read the notes beside every image and bring your questions to your next visit.</p>
  </div>
  <h2 class="section-title large" style="left:284px;top:114px">Vision</h2>
  <div class="section-body" style="left:284px;top:127px;width:70px">
    <p>Blurred or double vision, light sensitivity and trouble focusing are common signs. The visual system links the eyes to the back of the brain.</p>
  </div>
</section>

<!-- Hormone -->
<section class="spread col-right row-1">
  <div class="head-art layer-hormone" role="img" aria-label="Blue translucent head in profile with the hormone centre highlighted in orange"></div>
  <h2 class="section-title small" style="left:300px;top:204px">hormone</h2>
  <div class="section-body" style="left:300px;top:212px;width:36px">
    <p>Glands deep in the brain guide sleep, mood and energy. An injury can upset this balance for weeks.</p>
  </div>
</section>

<!-- Vestibular -->
<section class="spread col-left row-2">
  <div class="head-art layer-vestibular" role="img" aria-label="Blue translucent head in profile with the vestibular area highlighted in orange"></div>
  <h2 class="section-title small" style="left:224px;top:203px">vestibular</h2>
  <div class="section-body" style="left:224px;top:211px;width:36px">
    <p>The inner ear and brainstem keep you steady. Dizziness and poor balance often follow a head injury.</p>
  </div>
</section>

<!-- Physiological -->
<section class="spread col-right row-2">
  <div class="head-art layer-physiological" role="img" aria-label="Blue translucent head in profile with the brain surface shown in grey and deeper structures in orange"></div>
  <h2 class="section-title small" style="left:338px;top:203px">physiological</h2>
  <div class="section-body" style="left:338px;top:211px;width:36px">
    <p>Headache, fatigue and changes in heart rate can appear as the body responds to strain on the brain.</p>
  </div>
</section>

<!-- Somatosensory -->
<section class="spread col-left row-3">
  <div class="head-art layer-somatosensory" role="img" aria-label="Blue translucent head in profile with the somatosensory pathway highlighted in orange"></div>
  <h2 class="section-title small" style="left:262px;top:203px">somatosensory</h2>
  <div class="section-body" style="left:262px;top:211px;width:36px">
    <p>Touch, pain and body position are sensed here. Numbness or tingling may be a warning sign.</p>
  </div>
</section>

<!-- Psychological -->
<section class="spread col-right row-3">
  <div class="head-art layer-psychological" role="img" aria-label="Blue translucent head in profile with the whole brain glowing red and orange"></div>
  <h2 class="section-title small" style="left:375px;top:202px">psychological</h2>
  <div class="section-body" style="left:375px;top:210px;width:36px">
    <p>Low mood, worry and irritability can follow an injury. Talk with your clinic if these feelings linger.</p>
  </div>
</section>

</body>
</html>
```